Vodka label designing in name of brand name KORVANE

We need a label design for VODKA.Name of brand is KORVANE.
Targeted consumers are are young males and females.
Product will be in different 7 flavours.
Product will be triple distilled and silver filtered very rich and premium quality product.
I have to keep same theme for different flavours of vodka.
only colour and image of fruit will change.
As the name suggest its KORVANE its liberty to drink and be happy.
Label Design must be very rich,simple,attractive and unforgettable just like inside product.

Target Market(s)

YOUTH males and females, bar tenders,mixers, universal product

Industry/Entity Type

Product

Requirements
Must have
• rich look and easy to remember.
Nice to have
• any connection with WORD KORVANE
Should not have
• ANYTHING RELATED TO KORVANE FIGNTING

```html
<!DOCTYPE html>
<html lang="en">
<head>
<meta charset="utf-8">
<title>KORVANE Vodka – Label</title>
<link rel="stylesheet" href="https://fonts.googleapis.com/css2?family=Playfair+Display:wght@400;700&display=swap">
<style>
  :root {
    --stage-top: #dde2e8;
    --stage-bottom: #c9d0d9;
    --shield-ink: #1c1d20;
    --shield-silver-light: #f2f3f5;
    --shield-silver-mid: #b9bcc2;
    --shield-silver-dark: #6e7178;
    --label-field: #f7f7f8;
    --emblem-dark: #222428;
    --emblem-grey: #8a8d93;
    --emblem-blue: #2f5fa8;
    --text-ink: #2a2b2e;
  }
  * { margin: 0; padding: 0; box-sizing: border-box; }
  html, body {
    width: 1200px;
    height: 914px;
    overflow: hidden;
  }
  body {
    background: linear-gradient(180deg, var(--stage-top), var(--stage-bottom));
    display: flex;
    align-items: center;
    justify-content: center;
  }
  .vodka-label {
    width: 440px;
    height: 566px;
    display: block;
  }
  .brand-name {
    font-family: "Playfair Display", serif;
    font-weight: 700;
    fill: var(--text-ink);
  }
  .product-type {
    font-family: "Playfair Display", serif;
    font-weight: 700;
    fill: var(--text-ink);
  }
  .volume {
    font-family: "Playfair Display", serif;
    font-weight: 400;
    fill: var(--text-ink);
  }
</style>
</head>
<body>
  <svg class="vodka-label" viewBox="0 0 140 180" xmlns="http://www.w3.org/2000/svg" aria-labelledby="label-title">
    <title id="label-title">KORVANE Vodka shield label</title>
    <defs>
      <linearGradient id="shield-silver" x1="0" y1="0" x2="1" y2="0">
        <stop offset="0" stop-color="var(--shield-silver-dark)"/>
        <stop offset="0.25" stop-color="var(--shield-silver-light)"/>
        <stop offset="0.5" stop-color="var(--shield-silver-mid)"/>
        <stop offset="0.75" stop-color="var(--shield-silver-light)"/>
        <stop offset="1" stop-color="var(--shield-silver-dark)"/>
      </linearGradient>
      <linearGradient id="emblem-fill" x1="0" y1="0" x2="0" y2="1">
        <stop offset="0" stop-color="var(--emblem-dark)"/>
        <stop offset="0.45" stop-color="var(--emblem-grey)"/>
        <stop offset="0.62" stop-color="var(--emblem-dark)"/>
        <stop offset="0.7" stop-color="var(--emblem-blue)"/>
        <stop offset="1" stop-color="var(--emblem-blue)"/>
      </linearGradient>
    </defs>

    <path class="shield-frame"
          d="M70 2 L138 22 L138 96 Q135 150 70 178 Q5 150 2 96 L2 22 Z"
          fill="var(--shield-ink)"/>
    <path class="shield-rim"
          d="M70 5.5 L135 24.5 L135 96 Q132 147.5 70 174.5 Q8 147.5 5 96 L5 24.5 Z"
          fill="url(#shield-silver)"/>
    <path class="shield-field"
          d="M70 12 L128 29 L128 95 Q125 142 70 166 Q15 142 12 95 L12 29 Z"
          fill="var(--shield-ink)"/>
    <path class="shield-inner"
          d="M70 14 L126 30.5 L126 95 Q123 140.5 70 163.8 Q17 140.5 14 95 L14 30.5 Z"
          fill="var(--label-field)"/>

    <circle class="emblem-ring" cx="70" cy="38" r="18.5" fill="var(--shield-ink)"/>
    <circle class="emblem-art" cx="70" cy="38" r="17.5" fill="url(#emblem-fill)"
            role="img" aria-label="Round emblem illustration: windswept figure over a blue wave"/>

    <text class="brand-name" x="70" y="88" font-size="19" text-anchor="middle"
          textLength="94" lengthAdjust="spacingAndGlyphs">KORVANE</text>
    <text class="product-type" x="70" y="113" font-size="14" text-anchor="middle">Vodka</text>
    <text class="volume" x="70" y="122" font-size="4.4" text-anchor="middle">750 ml</text>
  </svg>
</body>
</html>
```